Business Cards Design for the electrical wholesaler: clean bold dynamic :)

We need a business card design that would follow our latest brand guidelines. As an electrical wholesaler we want to bring a fresh look and feel into the industry. The design should be clean bold and dynamic. It should come alive with the renewed energy of our green colour. Our grey colour should keep things balanced and complement the notion of maturity and responsibility. We employ Lato as a corporate font however are not bound by this font and we’re open to interpretation here.

Target Market(s)

Electrical contractors

Industry/Entity Type

Business

Contact Information for Business Card

Logo
Name & Surname: Olena Dovbush
Job Title: Director of Marketing
Email: helen.dovbush@mailvane.example
Cell phone: XXX.XXX.XXXX
Address: 20917 - 87 Ave. Edmonton, AB, Canada. T6K 2R8
Business Phone: 780.555.0187
Website: www.qorvil.example

Font styles to use
Other font styles liked:
• Lato

Requirements
Must have
• Logo & website
Nice to have
• Brand elements - some of them you may find in the attached Brand Guidelines (e.g. three lines on the background signifying "W")

```html
<!DOCTYPE html>
<html lang="en">
<head>
<meta charset="utf-8">
<title>Qorvil Business Card</title>
<link rel="stylesheet" href="https://fonts.googleapis.com/css2?family=Lato:wght@300;400;700;900&display=swap">
<style>
  :root {
    --brand-green: #8bc142;
    --brand-grey: #555759;
    --white: #ffffff;
  }
  html, body {
    margin: 0;
    padding: 0;
    width: 1017px;
    height: 1200px;
    overflow: hidden;
    background: var(--brand-green);
  }
  .card {
    position: relative;
    width: 1017px;
    height: 1200px;
    overflow: hidden;
    background: var(--brand-green);
    font-family: "Lato", sans-serif;
  }
  .card__panel {
    position: absolute;
    left: 0;
    top: 0;
  }
  .identity {
    position: absolute;
    left: 70px;
    top: 170px;
    color: var(--white);
  }
  .wordmark-small {
    display: flex;
    align-items: center;
    gap: 14px;
    font-weight: 400;
    font-size: 60px;
    line-height: 1;
    color: var(--white);
  }
  .wordmark-small__mark {
    width: 40px;
    height: 40px;
    background: var(--brand-green);
  }
  .identity__name {
    margin: 28px 0 0;
    font-weight: 700;
    font-size: 41px;
    line-height: 1;
    letter-spacing: 0.5px;
  }
  .identity__title {
    margin: 8px 0 0;
    font-weight: 400;
    font-size: 29px;
    line-height: 1.1;
    letter-spacing: 0.5px;
  }
  .address {
    position: absolute;
    left: 563px;
    top: 180px;
    width: 420px;
    margin: 0;
    font-weight: 900;
    font-size: 29px;
    line-height: 39px;
    color: var(--white);
    font-style: normal;
  }
  .address-rule {
    position: absolute;
    left: 563px;
    top: 266px;
    width: 400px;
    height: 3px;
    background: var(--brand-grey);
  }
  .contacts {
    position: absolute;
    left: 600px;
    top: 278px;
    width: 400px;
    margin: 0;
    padding: 0;
    list-style: none;
    font-weight: 400;
    font-size: 25px;
    letter-spacing: 0.3px;
    color: var(--brand-grey);
    white-space: nowrap;
  }
  .contacts li {
    height: 54px;
    line-height: 36px;
  }
  .brand-lockup {
    position: absolute;
    left: 240px;
    top: 830px;
    display: flex;
    align-items: flex-start;
    gap: 28px;
  }
  .brand-lockup__mark {
    width: 128px;
    height: 128px;
    margin-top: 4px;
    border-radius: 50%;
    background: var(--white);
  }
  .brand-lockup__name {
    display: block;
    font-weight: 400;
    font-size: 128px;
    line-height: 104px;
    color: var(--brand-grey);
    letter-spacing: 1px;
  }
  .brand-lockup__tagline {
    display: block;
    margin-top: 14px;
    font-weight: 700;
    font-size: 20px;
    letter-spacing: 2.6px;
    color: var(--brand-grey);
  }
</style>
</head>
<body>
  <main class="card">
    <svg class="card__panel" width="1017" height="1200" viewBox="0 0 1017 1200" aria-hidden="true">
      <path fill="var(--brand-grey)" d="M0 0 H370 C430 0 465 40 480 95 L610 480 C630 535 645 560 668 567 C640 590 610 600 575 600 H0 Z"/>
    </svg>

    <section class="identity">
      <div class="wordmark-small"><span class="wordmark-small__mark"></span>qorvil</div>
      <h1 class="identity__name">Olena Dovbush</h1>
      <p class="identity__title">Director of Marketing</p>
    </section>

    <address class="address">20917 - 87 Ave. Edmonton,<br>AB, Canada. T6K 2R8</address>
    <div class="address-rule"></div>

    <ul class="contacts">
      <li>helen.dovbush@mailvane.example</li>
      <li>780.555.0187</li>
      <li>www.qorvil.example</li>
    </ul>

    <div class="brand-lockup">
      <span class="brand-lockup__mark"></span>
      <div>
        <span class="brand-lockup__name">qorvil</span>
        <span class="brand-lockup__tagline">ELECTRICAL WHOLESALERS</span>
      </div>
    </div>
  </main>
</body>
</html>
```